Real Estate Acquisition Company Needs Business Card Design

Tellwyn Real Estate is in need of a business card design!

As a Real Estate Acquisition Company, Tellwyn Real Estate conducts mutually beneficial real estate transactions that actively consider the needs of the seller. At Tellwyn Real Estate we’re actively buying properties from those that see value in a direct transaction, but more importantly want reassurances that they, personally, are in integral part of it. Of course, it all starts with fair market value, but it doesn’t stop there. We’ve found the most success when we offer more. And with our deep experience in this industry, we’ve discovered that we have a lot to offer!

We already have a logo and brand guidelines that we've uploaded. Our final design should stay true to the guidelines. We are looking for a business card design that has two names (Ex. Jane Doe & John Doe) and contact information for each person- this way the company principals can share a card as they often do business as a team.
Updates

The criteria was unfortunately not met on most designs. We are looking for a card that has a layout for TWO names and respective contact information for each of the two people. Almost all designs only had a space for one name and one set of contact information.

Industry/Entity Type

Real Estate

Contact Information for Business Card

We are looking for a business card design that has two names (Ex. Jane Doe & John Doe) and each of their contact information- this way the company principals can share a card as they often do business as a team.

Font styles to use
Other font styles liked:
• Use Brand Guidelines

Requirements
Must have
• Please stay true to our Brand Guidelines for colours, fonts, and positioning of logo.

We require a layout for two names and respective contact information. The company principals work as a team and want a card that has both their information on it.

```html
<!DOCTYPE html>
<html lang="en">
<head>
<meta charset="utf-8">
<title>Tellwyn Real Estate – Business Card</title>
<link rel="stylesheet" href="https://fonts.googleapis.com/css2?family=Open+Sans:wght@400;600;700&display=swap">
<style>
  :root {
    --bg: #1c1f24;
    --card: #3b3b3c;
    --card-dark: #141412;
    --gold: #eda21f;
    --white: #ffffff;
    --grey: #c9c9c9;
  }
  * { margin: 0; padding: 0; box-sizing: border-box; }
  html, body { width: 1200px; height: 900px; overflow: hidden; }
  body {
    background: var(--bg);
    font-family: "Open Sans", Arial, sans-serif;
    display: flex;
    flex-direction: column;
    align-items: center;
    justify-content: center;
    gap: 56px;
  }
  .card {
    position: relative;
    width: 600px;
    height: 343px;
    border-radius: 22px;
    background: var(--card);
    overflow: hidden;
    box-shadow: 0 14px 30px rgba(0,0,0,.45);
  }
  .card__wedges { position: absolute; inset: 0; width: 100%; height: 100%; }
  .card__wedges polygon { fill: var(--card-dark); }

  /* front */
  .card--front .brand-name {
    position: absolute;
    left: 0; right: 0; top: 142px;
    text-align: center;
    color: var(--white);
    font-weight: 600;
    font-size: 40px;
    letter-spacing: 2px;
    text-transform: uppercase;
    line-height: 1;
  }
  .card--front .brand-name span { display: block; font-size: 15px; letter-spacing: 5px; margin-top: 10px; }

  /* back */
  .card--back .brand-name {
    position: absolute;
    left: 92px; top: 26px;
    color: var(--white);
    font-weight: 600;
    font-size: 22px;
    letter-spacing: 1px;
    text-transform: uppercase;
    line-height: 1;
  }
  .card--back .brand-name span { display: block; font-size: 8px; letter-spacing: 3px; margin-top: 5px; text-align: right; }
  .person { position: absolute; }
  .person--jane { left: 120px; top: 92px; }
  .person--john { left: 340px; top: 186px; }
  .person__name { color: var(--gold); font-weight: 700; font-size: 22px; line-height: 1.1; }
  .person__role {
    color: var(--grey); font-size: 14px;
    padding-bottom: 4px; margin-bottom: 9px;
    border-bottom: 2px solid var(--gold);
    width: 132px;
  }
  .contact { list-style: none; }
  .contact li {
    display: flex; align-items: center; gap: 10px;
    color: var(--white); font-weight: 600; font-size: 12px;
    margin-bottom: 6px;
  }
  .contact svg { width: 15px; height: 15px; flex: none; }
</style>
</head>
<body>

  <section class="card card--front" aria-label="Card front">
    <svg class="card__wedges" viewBox="0 0 600 343" preserveAspectRatio="none" aria-hidden="true">
      <polygon points="0,90 0,343 150,343"/>
      <polygon points="600,0 600,300 470,0"/>
    </svg>
    <div class="brand-name">Tellwyn<span>Real Estate Inc.</span></div>
  </section>

  <section class="card card--back" aria-label="Card back">
    <svg class="card__wedges" viewBox="0 0 600 343" preserveAspectRatio="none" aria-hidden="true">
      <polygon points="0,70 0,343 175,343"/>
      <polygon points="600,0 600,250 500,0"/>
    </svg>

    <div class="brand-name">Tellwyn<span>Real Estate Inc.</span></div>

    <div class="person person--jane">
      <p class="person__name">Ex. Jane Doe</p>
      <p class="person__role">Designation</p>
      <ul class="contact">
        <li><svg viewBox="0 0 16 16"><rect width="16" height="16" rx="2" fill="#eda21f"/><path d="M5 3.5l2 2-1 1.2a6 6 0 0 0 3.3 3.3l1.2-1 2 2-1.2 1.5C7.5 12.5 3.5 8.5 3.5 4.7z" fill="#fff"/></svg>+000 000 2866</li>
        <li><svg viewBox="0 0 16 16"><rect width="16" height="16" rx="2" fill="#eda21f"/><rect x="3.5" y="5" width="9" height="6.5" fill="#fff"/><path d="M3.5 5l4.5 3.5L12.5 5" stroke="#eda21f" fill="none"/></svg>hello@Example.com</li>
        <li><svg viewBox="0 0 16 16"><rect width="16" height="16" rx="2" fill="#eda21f"/><circle cx="8" cy="8" r="4.5" fill="none" stroke="#fff" stroke-width="1.2"/><path d="M3.5 8h9M8 3.5c-2 2.5-2 6.5 0 9M8 3.5c2 2.5 2 6.5 0 9" stroke="#fff" fill="none"/></svg>www.tellwynre.com</li>
      </ul>
    </div>

    <div class="person person--john">
      <p class="person__name">John Doe</p>
      <p class="person__role">Designation</p>
      <ul class="contact">
        <li><svg viewBox="0 0 16 16"><rect width="16" height="16" rx="2" fill="#eda21f"/><path d="M5 3.5l2 2-1 1.2a6 6 0 0 0 3.3 3.3l1.2-1 2 2-1.2 1.5C7.5 12.5 3.5 8.5 3.5 4.7z" fill="#fff"/></svg>+000 000 2866</li>
        <li><svg viewBox="0 0 16 16"><rect width="16" height="16" rx="2" fill="#eda21f"/><rect x="3.5" y="5" width="9" height="6.5" fill="#fff"/><path d="M3.5 5l4.5 3.5L12.5 5" stroke="#eda21f" fill="none"/></svg>hello@Example.com</li>
        <li><svg viewBox="0 0 16 16"><rect width="16" height="16" rx="2" fill="#eda21f"/><circle cx="8" cy="8" r="4.5" fill="none" stroke="#fff" stroke-width="1.2"/><path d="M3.5 8h9M8 3.5c-2 2.5-2 6.5 0 9M8 3.5c2 2.5 2 6.5 0 9" stroke="#fff" fill="none"/></svg>www.tellwynre.com</li>
      </ul>
    </div>
  </section>

</body>
</html>
```